Garden Maintenance business card

I need a business card design for my new business "Silver Birch Garden Co". I do garden maintenance including lawns, turf lawn, pruning, hedging, water systems, anything related to the garden really (dont think i need to include any of that except garden maintenance)

Reason: narrowed it down and just showing my business partners the designs, cheers

Industry/Entity Type

Business

Requirements
Must have
• Must Have:
- ABN: XX XXX XXX XXX
Mobile phone number 00 0000000
email address xxxx.xxxxxx@leafpost.net
Owner Name Xxxx xxxxxx
title: garden specialist possibly under name or something sounding professional
logo which has been submitted both with a background and one without, feel free to choose whichever one you like
business name

```html
<!DOCTYPE html>
<html lang="en">
<head>
<meta charset="utf-8">
<title>Silver Birch Garden Co – Business Card</title>
<link href="https://fonts.googleapis.com/css2?family=Anton&family=Arimo:ital,wght@0,400;1,400&display=swap" rel="stylesheet">
<style>
  :root {
    --page-bg: #f2f2f2;
    --front-green: #127a1a;
    --front-green-light: #1b8f24;
    --front-green-dark: #0d6314;
    --front-text: #ffffff;
    --back-bg: #ffffff;
    --grain-light: #f4f8e8;
    --grain-mid: #e3ecc8;
    --back-title: #1f8a1c;
    --back-olive: #8c8a06;
    --icon-green: #2a8a25;
    --flower-white: #f5f7ee;
    --flower-green: #8cc63f;
    --card-shadow: rgba(0, 0, 0, 0.25);
  }
  * { margin: 0; padding: 0; box-sizing: border-box; }
  html, body {
    width: 1171px;
    height: 1200px;
    overflow: hidden;
    background: var(--page-bg);
  }
  .canvas {
    width: 1171px;
    height: 1200px;
    display: flex;
    flex-direction: column;
    align-items: center;
    justify-content: center;
    gap: 60px;
  }
  .card {
    position: relative;
    width: 960px;
    height: 540px;
    border-radius: 6px;
    overflow: hidden;
    box-shadow: 0 6px 18px var(--card-shadow);
  }
  .business-name {
    position: absolute;
    left: 0;
    width: 100%;
    text-align: center;
    font-family: "Anton", "Impact", sans-serif;
    font-weight: 400;
    font-size: 70px;
    line-height: 1;
    white-space: nowrap;
  }
  .tagline {
    position: absolute;
    font-family: "Arimo", "Arial", sans-serif;
    font-style: italic;
    font-size: 26px;
    line-height: 1.3;
    text-align: center;
  }
  .detail {
    position: absolute;
    font-family: "Arimo", "Arial", sans-serif;
    font-size: 26px;
    line-height: 1.3;
    white-space: nowrap;
  }

  /* Front side */
  .card--front {
    background: linear-gradient(160deg, var(--front-green-light) 0%, var(--front-green) 45%, var(--front-green-dark) 100%);
    color: var(--front-text);
  }
  .card--front .business-name { top: 70px; padding-left: 60px; }
  .card--front .tagline { top: 170px; left: 340px; width: 480px; }
  .card--front .owner { bottom: 80px; left: 300px; }
  .flower-illustration {
    position: absolute;
    left: 60px;
    top: 270px;
    width: 200px;
    height: 120px;
    border-radius: 50%;
    background: radial-gradient(ellipse at 45% 50%, rgba(245, 247, 238, 0.85) 0%, rgba(140, 198, 63, 0.6) 45%, rgba(140, 198, 63, 0) 72%);
  }

  /* Back side */
  .card--back { background: var(--back-bg); }
  .wood-grain {
    position: absolute;
    inset: 0;
    background: linear-gradient(100deg, var(--grain-light) 0%, var(--grain-mid) 30%, var(--grain-light) 55%, var(--grain-mid) 80%, var(--grain-light) 100%);
    opacity: 0.9;
  }
  .card--back .business-name { top: 80px; color: var(--back-title); }
  .card--back .tagline { top: 190px; left: 240px; width: 480px; color: var(--back-olive); }
  .back-info { color: var(--back-olive); }
  .owner-block { top: 340px; left: 560px; }
  .owner-block .label { display: inline-block; width: 92px; }
  .contact-block { left: 80px; top: 400px; }
  .contact-row {
    display: flex;
    align-items: center;
    gap: 14px;
    height: 42px;
  }
  .contact-icon {
    flex: none;
    width: 24px;
    display: flex;
    justify-content: center;
  }
</style>
</head>
<body>
<main class="canvas">

  <section class="card card--front" aria-label="Business card front">
    <h1 class="business-name">Silver Birch Garden Co</h1>
    <p class="tagline">The Garden Maintenance Specialist<br>at your service !</p>
    <div class="flower-illustration" role="img" aria-label="Illustration of white daisies and green clover leaves"></div>
    <p class="detail owner">Owner&nbsp; Xxxx xxxxxx</p>
  </section>

  <section class="card card--back" aria-label="Business card back">
    <div class="wood-grain" role="img" aria-label="Faint pale green wood grain texture"></div>
    <h2 class="business-name">Silver Birch Garden Co</h2>
    <p class="tagline">The Garden Maintenance Specialist<br>at your service !</p>

    <div class="detail back-info owner-block">
      <div><span class="label">Owner</span>Xxxx xxxxxx</div>
      <div><span class="label">ABN:</span>XX XXX XXX XXX</div>
    </div>

    <div class="detail back-info contact-block">
      <div class="contact-row">
        <span class="contact-icon">
          <svg width="20" height="30" viewBox="0 0 20 30" aria-hidden="true">
            <rect x="1" y="1" width="18" height="28" rx="3" fill="none" stroke="var(--icon-green)" stroke-width="2"/>
            <rect x="4" y="5" width="12" height="10" fill="var(--icon-green)"/>
            <circle cx="10" cy="23" r="2" fill="var(--icon-green)"/>
          </svg>
        </span>
        <span>00 0000000</span>
      </div>
      <div class="contact-row">
        <span class="contact-icon">
          <svg width="24" height="18" viewBox="0 0 24 18" aria-hidden="true">
            <rect x="1" y="1" width="22" height="16" fill="var(--icon-green)"/>
            <path d="M1 1 L12 10 L23 1" fill="none" stroke="#ffffff" stroke-width="2"/>
          </svg>
        </span>
        <span>xxxx.xxxxxx@leafpost.net</span>
      </div>
    </div>
  </section>

</main>
</body>
</html>
```